Postcard Design

We are a pet resort located near Atlanta's Corbinvale Pruett Airport. I want a postcard that will show dogs playing and the offer will be "New customers receive 50% off boarding" *
* 50% offer applies to standard lodging fees only. Amenities and playtimes not included in this offer. Valid for up to 10 nights of boarding. Blackout dates of July 4th, Thanksgiving week and Christmas week apply. Reservations required.
The backside of the postcard will read, "New daycare customers recieve ONE WEEK of FREE daycare for your dog".*
* offer good for 5 consecutive days of daycare only-not in conjuction with overnight lodging. Good for one pet per family only. Offer not valid on July 4th week, Thanksgiving week or Christmas week.

```html
<!DOCTYPE html>
<html lang="en">
<head>
<meta charset="utf-8">
<title>New Customers Receive 50% Off Boarding</title>
<link rel="stylesheet" href="https://fonts.googleapis.com/css2?family=Alfa+Slab+One&family=Cutive&display=swap">
<style>
  :root {
    --paper: #ffffff;
    --orange: #ee6a3e;
    --plum: #3e2b52;
    --plum-soft: #5a4670;
    --bar-light: #ece8f0;
    --pattern-warm: #fde6d8;
    --pattern-cool: #e3f1f3;
    --pattern-leaf: #eef4d6;
    --pattern-lilac: #ebe6f1;
  }
  * { margin: 0; padding: 0; box-sizing: border-box; }
  html, body { width: 1200px; height: 937px; overflow: hidden; background: var(--paper); }
  .postcard {
    position: relative;
    width: 1200px;
    height: 937px;
    overflow: hidden;
    background: var(--paper);
  }
  .pattern-field {
    position: absolute;
    inset: 0;
    background:
      radial-gradient(circle at 8% 12%, var(--pattern-warm) 0, transparent 16%),
      radial-gradient(circle at 92% 10%, var(--pattern-cool) 0, transparent 15%),
      radial-gradient(circle at 5% 60%, var(--pattern-lilac) 0, transparent 14%),
      radial-gradient(circle at 95% 55%, var(--pattern-lilac) 0, transparent 15%),
      radial-gradient(circle at 12% 92%, var(--pattern-warm) 0, transparent 14%),
      radial-gradient(circle at 88% 92%, var(--pattern-leaf) 0, transparent 15%),
      radial-gradient(circle at 50% 45%, var(--pattern-warm) 0, transparent 35%),
      var(--paper);
  }
  .headline {
    position: absolute;
    left: 0;
    width: 100%;
    text-align: center;
    font-family: "Alfa Slab One", serif;
    color: var(--orange);
  }
  .headline-lead {
    top: 150px;
    font-size: 50px;
    letter-spacing: 2px;
    text-shadow: 2px 2px 0 var(--plum);
  }
  .headline-offer {
    top: 212px;
    font-size: 142px;
    line-height: 1;
    letter-spacing: 4px;
    text-shadow: 6px 6px 0 var(--plum);
  }
  .headline-service {
    top: 372px;
    left: 380px;
    width: 500px;
    font-size: 66px;
    letter-spacing: 2px;
    transform: rotate(-3deg);
    text-shadow: 3px 3px 0 var(--plum);
    z-index: 2;
  }
  .dogs-scene {
    position: absolute;
    left: 250px;
    top: 366px;
    width: 760px;
    height: 238px;
    background: linear-gradient(180deg, rgba(90,70,112,0.10), rgba(90,70,112,0.22));
    border-radius: 8px;
  }
  .ground-bar {
    position: absolute;
    left: 172px;
    top: 528px;
    width: 856px;
    height: 18px;
    background: linear-gradient(180deg, var(--plum-soft), var(--bar-light));
    z-index: 1;
  }
  .terms {
    position: absolute;
    left: 0;
    width: 100%;
    text-align: center;
    font-family: "Cutive", serif;
    color: var(--plum);
  }
  .terms-main {
    top: 612px;
    font-size: 26px;
    line-height: 36px;
    font-weight: 700;
  }
  .terms-fine {
    top: 752px;
    font-size: 19px;
    line-height: 34px;
  }
</style>
</head>
<body>
  <main class="postcard">
    <div class="pattern-field" role="img" aria-label="Scattered paw prints and dog bones in orange, teal, green and purple"></div>

    <h1 class="headline headline-lead">NEW CUSTOMERS RECEIVE</h1>
    <p class="headline headline-offer">50% OFF</p>

    <div class="dogs-scene" role="img" aria-label="Silhouettes of five dogs playing together on a ground line"></div>
    <div class="ground-bar"></div>
    <p class="headline headline-service">BOARDING!</p>

    <p class="terms terms-main">
      50% offer applies to standard lodging fees only.<br>
      Amenities and playtimes not included in this offer.<br>
      Valid for up to 10 nights of boarding.
    </p>
    <p class="terms terms-fine">
      Blackout dates of July 4th, Thanksgiving week and<br>
      Christmas week apply. Reservations required.
    </p>
  </main>
</body>
</html>
```